BRAND NEW EVENT SALTWAVE IBIZA BOAT PARTY FLYER/POSTER

Saltwave Ibiza
Presents:
The Saltwave Ibiza Boat Party
Launch date: 18.05.22
We need a flyer/poster making to advertise our new boat party launching this summer in Ibiza. We are going all-out with the event, therefore we need to showcase this in our advertisement.
We have some of Ibiza's most famous resident DJs playing house/tech music for 4 hours on the boat, which leaves from San Antonio in Ibiza at 5.30pm. The boat holds 200 people!
There will also be professional dancers, who will perform a fire show LED show and act as VIP hostesses for guests. We will also have a full film crew who will be making a promotional video for us on the day.
Feel free to include some, all of none of the above. Be creative!
The poster needs to scream a VIP, high-end boat party with good music and good vibes. It needs to look professional and resonate with who we are - Saltwave Ibiza. It needs to be classy and memorable.
I'm open to ideas! I've included our logo and some photos of the boat/Ibiza in general for inspirational purposes.
Please use your own initiative and don’t just use the photos I’ve sent with some simple writing on it. 😉
Please let me know what you come up with - we need something urgently!
Kind regards,
Saltwave Ibiza Team
Target Market(s)
Young party-goers on holiday in Ibiza
Industry/Entity Type
Events

```html
<!DOCTYPE html>
<html lang="en">
<head>
<meta charset="utf-8">
<title>Saltwave Ibiza Boat Party</title>
<link href="https://fonts.googleapis.com/css2?family=Montserrat:wght@400;500;600;700;800&family=Kaushan+Script&family=Roboto:ital,wght@0,400;0,500;1,700&display=swap" rel="stylesheet">
<style>
  :root{
    --night:#0c0716;
    --plum:#2a0f33;
    --violet:#4a1a55;
    --magenta:#b43fa8;
    --orchid:#9c3c9f;
    --pink:#e0206a;
    --cream:#fff3cf;
    --gold:#d59a52;
    --white:#ffffff;
    --muted:#4d4a6d;
  }
  *{margin:0;padding:0;box-sizing:border-box}
  html,body{width:776px;height:1200px;overflow:hidden;background:var(--night)}
  .poster{position:relative;width:776px;height:1200px;overflow:hidden;font-family:'Montserrat',sans-serif;color:var(--white);
    background:linear-gradient(180deg,var(--plum) 0%,#1d0a26 55%,var(--night) 100%)}
  .backdrop{position:absolute;inset:0 0 480px 0;
    background:radial-gradient(ellipse at 50% 42%,#5a2460 0%,#3a1444 38%,#1b0a24 75%,transparent 100%)}
  .ring{position:absolute;left:0;top:0}
  .presents{position:absolute;top:106px;width:100%;text-align:center;font-weight:700;font-size:20px;letter-spacing:7px;padding-left:7px}
  .brand{position:absolute;top:236px;width:100%;text-align:center;font-weight:700;font-size:42px;color:var(--magenta)}
  .title{position:absolute;top:392px;width:100%;text-align:center;font-family:'Kaushan Script',cursive;font-size:138px;line-height:1;
    color:var(--white);transform:rotate(-4deg);
    -webkit-text-stroke:3px var(--pink);paint-order:stroke fill;
    text-shadow:0 4px 0 #b01650,0 7px 0 #8e1242,0 12px 18px rgba(0,0,0,.6)}
  .launch{position:absolute;top:668px;width:100%;text-align:center;font-weight:600;font-size:46px;color:var(--orchid);letter-spacing:.5px}
  .tagline{position:absolute;top:733px;width:100%;text-align:center;font-weight:700;font-size:26px;line-height:36px;color:var(--cream)}
  .glow{position:absolute;left:90px;width:596px;height:2px;background:linear-gradient(90deg,transparent,#f1b98a 50%,transparent);box-shadow:0 0 10px #ffcfa0}
  .glow.upper{top:823px}
  .glow.lower{top:983px}
  .features{position:absolute;top:840px;left:0;width:100%;height:110px}
  .feature{position:absolute;top:0;height:110px}
  .divider{position:absolute;top:0;width:1px;height:110px;background:rgba(255,255,255,.35)}
  .f-boat{left:78px;top:6px}
  .f-boat .small{font-size:15px;font-weight:700}
  .f-boat .big{font-size:30px;font-weight:800;margin-top:2px}
  .f-boat .accent{font-size:15px;font-weight:700;color:var(--orchid);margin-top:10px}
  .f-dance{left:316px;top:12px}
  .f-dance .head{font-size:20px;font-weight:700;line-height:24px}
  .f-dance .accent{font-size:16px;font-weight:700;color:var(--orchid);line-height:19px;margin-top:4px}
  .f-djs{left:528px;top:4px}
  .f-djs .head{font-size:28px;font-weight:700;color:#efe6f7}
  .f-djs .accent{font-size:16px;color:var(--orchid);margin-top:1px}
  .f-djs .small{font-size:15px;margin-top:4px}
  .departure{position:absolute;top:1038px;width:100%;text-align:center;font-size:17px}
  .departure b{font-weight:700}
  .contact{position:absolute;top:1072px;width:100%;text-align:center;font-family:'Roboto',sans-serif;font-size:23px;font-weight:500;color:var(--orchid)}
  .contact .phone{font-style:italic;font-weight:700;font-size:26px}
  .links{position:absolute;top:1119px;width:100%;text-align:center;font-family:'Roboto',sans-serif;font-size:16px;color:var(--muted)}
</style>
</head>
<body>
<div class="poster">
  <div class="backdrop" role="img" aria-label="Night sky full of pink and gold fireworks, sparks and confetti"></div>
  <svg class="ring" width="776" height="720" viewBox="0 0 776 720" aria-hidden="true">
    <defs>
      <linearGradient id="ringStroke" x1="0" y1="0" x2="1" y2="1">
        <stop offset="0" stop-color="#e0a860"/>
        <stop offset=".5" stop-color="#d0604a"/>
        <stop offset="1" stop-color="#c98a4c"/>
      </linearGradient>
    </defs>
    <circle cx="408" cy="318" r="282" fill="none" stroke="url(#ringStroke)" stroke-width="5" opacity=".85"/>
  </svg>

  <div class="presents">PRESENTS</div>
  <div class="brand">Saltwave Ibiza</div>
  <div class="title">Boat Party</div>

  <div class="launch">LAUNCH DATE: 18.05.22</div>
  <div class="tagline">VIP, HIGH-END BOAT PARTY WITH<br>GOOD MUSIC AND GOOD VIBES.</div>

  <div class="glow upper"></div>
  <div class="features">
    <div class="feature f-boat">
      <div class="small">The boat holds</div>
      <div class="big">200 people!</div>
      <div class="accent">VIP hostesses for guests</div>
    </div>
    <div class="divider" style="left:296px"></div>
    <div class="feature f-dance">
      <div class="head">PROFESSIONAL<br>DANCERS</div>
      <div class="accent">FIRE SHOW<br>LED SHOW</div>
    </div>
    <div class="divider" style="left:502px"></div>
    <div class="feature f-djs">
      <div class="head">DJs playing</div>
      <div class="accent">house/tech music</div>
      <div class="small">for 4 hours on the boat</div>
    </div>
  </div>
  <div class="glow lower"></div>

  <div class="departure">LEAVES FROM <b>SAN ANTONIO</b> IN IBIZA AT 5.30PM.</div>
  <div class="contact">For more Info Call Us Now <span class="phone">07700914382</span></div>
  <div class="links">www.saltwaveibiza.com &nbsp;|&nbsp; hello@saltwavemail.com</div>
</div>
</body>
</html>
```